Postcard Design for Brindlewood Pine Acres LLC

We are a small family owned Christmas tree farm. We work with various groups on their fundraising programs selling wreaths and trees. Our goal is to expand our business, advertising with post cards.

Target Market(s)

Schools, Trail Rangers, various non profit groups

Industry/Entity Type

Advertising

Requirements
Must have
• Front side-

Let us help you develop a successful holiday fundraiser for your group with fresh, fragrant Wisconsin wreaths shipped directly from our farm!

Picture of a real wreath with a red bow and 2 pinecone clusters at 4 o'clock and 8 o'clock.

Contact information -
Brindlewood Pine Acres LLC
www.brindlewoodpineacres.com
555-147-9362

Backside -
We have 2 different type of wreath fundraising programs - mail order and direct distribution. You group can choose to do one or both. Wholesale Christmas trees are also available.

```html
<!DOCTYPE html>
<html lang="en">
<head>
<meta charset="utf-8">
<title>Brindlewood Pine Acres – Fundraiser Postcard</title>
<link href="https://fonts.googleapis.com/css2?family=Open+Sans:wght@400;700&display=swap" rel="stylesheet">
<style>
  :root{
    --backdrop:#d9dcdb;
    --wood-dark:#4a1d12;
    --wood-mid:#7a3422;
    --wood-light:#9c4a30;
    --frame:#f1ebe1;
    --farm-green:#3e6b1f;
    --card-white:#f3f4f2;
    --line-green:#2f7a2c;
    --text-light:#ffffff;
    --photo-dark:#4c4e4c;
    --photo-light:#d2d3d1;
  }
  *{box-sizing:border-box;margin:0;padding:0}
  html,body{width:1200px;height:1000px;overflow:hidden}
  body{
    background:var(--backdrop);
    font-family:"Open Sans",sans-serif;
    display:flex;flex-direction:column;align-items:center;justify-content:center;gap:40px;
  }
  .postcard{
    position:relative;width:660px;height:440px;overflow:hidden;
    box-shadow:0 6px 18px rgba(0,0,0,.18);
  }

  /* Front */
  .front{background:var(--frame);padding:14px}
  .front__photo{
    position:absolute;inset:14px;
    background:
      radial-gradient(circle at 50% 28%, #2f4a1e 0 70px, #23381a 90px, transparent 120px),
      linear-gradient(90deg,var(--wood-dark),var(--wood-light) 20%,var(--wood-mid) 40%,var(--wood-light) 60%,var(--wood-mid) 80%,var(--wood-dark));
  }
  .front__banner{
    position:absolute;left:14px;bottom:52px;width:370px;
    background:var(--farm-green);color:var(--text-light);
    padding:12px 30px 12px 22px;
    clip-path:polygon(0 0,100% 0,93% 50%,100% 100%,0 100%);
    font-weight:700;font-size:15px;line-height:1.3;
  }
  .front__contact{
    position:absolute;right:36px;bottom:150px;text-align:left;
    color:var(--text-light);font-size:10px;line-height:1.45;
  }
  .front__contact .phone{font-weight:700;font-size:11px}

  /* Back */
  .back{background:var(--card-white);display:flex}
  .back__photo-side{
    position:relative;width:50%;height:100%;
    background:linear-gradient(180deg,var(--photo-dark) 0%,#5e605e 45%,#8c8e8c 62%,var(--photo-light) 100%);
  }
  .back__copy{
    position:absolute;left:26px;top:22px;right:22px;
    color:var(--text-light);font-weight:700;font-size:13.5px;line-height:1.35;text-align:justify;
  }
  .back__brand{
    position:absolute;left:24px;bottom:0;width:136px;height:104px;
    background:var(--farm-green);border-radius:68px 68px 0 0;
    color:var(--text-light);text-align:center;padding-top:24px;
  }
  .back__brand-name{font-size:14px;line-height:1.15;font-weight:400}
  .back__brand-web{font-size:6.5px;margin-top:12px}
  .back__address-side{position:relative;width:50%;height:100%}
  .back__stamp{
    position:absolute;right:34px;top:26px;width:104px;height:96px;
    border:2px solid var(--line-green);
  }
  .back__lines{position:absolute;left:34px;right:34px;top:178px}
  .back__lines span{display:block;height:2px;background:var(--line-green);margin-bottom:40px}
</style>
</head>
<body>

  <section class="postcard front" aria-label="Postcard front">
    <div class="front__photo" role="img" aria-label="Photo of a fresh evergreen wreath with a red bow and pinecone clusters hanging on a dark wooden door"></div>
    <p class="front__banner">Let us help you develop a successful holiday fundraiser for your group with fresh, fragrant Wisconsin wreaths shipped directly from our farm!</p>
    <div class="front__contact">
      <p>Brindlewood Pine Acres LLC</p>
      <p>www.brindlewoodpineacres.com</p>
      <p class="phone">555-147-9362</p>
    </div>
  </section>

  <section class="postcard back" aria-label="Postcard back">
    <div class="back__photo-side" role="img" aria-label="Black and white photo of rows of Christmas trees growing on the farm">
      <p class="back__copy">We have 2 different type of wreath fundraising programs, mail order and direct distribution. You group can choose to do one or both. Wholesale Christmas trees are also available.</p>
      <div class="back__brand">
        <p class="back__brand-name">Brindlewood<br>Pine Acres</p>
        <p class="back__brand-web">www.brindlewoodpineacres.com</p>
      </div>
    </div>
    <div class="back__address-side">
      <div class="back__stamp"></div>
      <div class="back__lines"><span></span><span></span><span></span><span></span><span></span></div>
    </div>
  </section>

</body>
</html>
```